Graphics for Corvella telehealth weight loss plans

Corvella focuses on delivering medical weight-loss using prescription medicine and telehealth consults. Corvella needs graphics for its ecommerce site for three weight loss plans. The plans are posted here with current graphics and descriptions of what is included with each plan. Please do not feel constrained by current graphics or styling.

- https://store.corvellacare.com/products/radiant-horizon-plan
- https://store.corvellacare.com/products/brightpath-core-plan
- https://store.corvellacare.com/products/daily-harbor-plan

The graphics need to look good on mobile and desktop browsers.

```html
<!DOCTYPE html>
<html lang="en">
<head>
<meta charset="utf-8">
<title>Daily Harbor Plan – Corvella</title>
<link rel="stylesheet" href="https://fonts.googleapis.com/css2?family=Assistant:wght@400;600;700&family=Oswald:wght@300;400;500;600&display=swap">
<style>
  :root {
    --page: #ffffff;
    --ink: #121212;
    --ink-soft: #4a4a4a;
    --navy: #25235e;
    --cyan: #20c7f1;
    --photo-dark: #4b4b4b;
    --photo-light: #bdbdbd;
    --button: #121212;
    --button-text: #ffffff;
  }
  * { margin: 0; padding: 0; box-sizing: border-box; }
  html, body { width: 1200px; height: 821px; overflow: hidden; background: var(--page); }
  body { position: relative; font-family: "Assistant", sans-serif; color: var(--ink); }

  .site-header { position: absolute; inset: 0 0 auto 0; height: 120px; }
  .brand { position: absolute; left: 73px; top: 62px; font-size: 20px; font-weight: 600; letter-spacing: .5px; color: var(--ink); line-height: 26px; }
  .nav { position: absolute; top: 64px; left: 162px; display: flex; gap: 0; font-size: 14.5px; letter-spacing: .6px; color: var(--ink-soft); line-height: 22px; }
  .nav a { color: inherit; text-decoration: none; position: absolute; white-space: nowrap; }
  .nav .chev { display: inline-block; vertical-align: middle; margin-left: 8px; }
  .header-icons { position: absolute; top: 63px; left: 1025px; }
  .header-icons svg { position: absolute; top: 0; }

  .product-graphic { position: absolute; left: 66px; top: 146px; width: 487px; height: 630px; background: var(--navy); overflow: hidden; }
  .photo { position: absolute; background: linear-gradient(100deg, var(--photo-dark) 0%, #8a8a8a 45%, var(--photo-light) 75%, #7a7a7a 100%); }
  .photo-top { left: 0; top: 0; width: 487px; height: 138px; }
  .photo-side { left: 357px; top: 138px; width: 130px; height: 63px; background: linear-gradient(180deg, #b0b0b0, #6e6e6e); }
  .graphic-title { position: absolute; left: 33px; top: 146px; font-family: "Oswald", sans-serif; font-weight: 600; font-size: 48px; line-height: 54px; color: var(--cyan); letter-spacing: .3px; }
  .includes-tag { position: absolute; left: 34px; top: 273px; width: 82px; height: 27px; background: var(--cyan); border-radius: 2px; font-family: "Oswald", sans-serif; font-weight: 500; font-size: 18px; line-height: 27px; text-align: center; color: var(--navy); }
  .graphic-list { position: absolute; left: 28px; top: 323px; list-style: none; font-family: "Oswald", sans-serif; font-weight: 500; font-size: 20.5px; color: var(--cyan); }
  .graphic-list li { position: absolute; white-space: nowrap; line-height: 28px; }
  .graphic-list li::before { content: "• "; font-size: 16px; }
  .graphic-list .aside { font-weight: 300; font-size: 16px; margin-left: 4px; }
  .graphic-note { position: absolute; left: 32px; top: 474px; font-family: "Oswald", sans-serif; font-weight: 300; font-size: 16px; color: var(--cyan); line-height: 22px; }
  .pay-badge { position: absolute; left: 86px; top: 553px; width: 241px; height: 26px; background: var(--cyan); border-radius: 2px; font-family: "Oswald", sans-serif; font-weight: 500; font-size: 17.5px; line-height: 26px; color: var(--navy); padding-left: 14px; }
  .pay-icon { position: absolute; left: 37px; top: 537px; }

  .product-info { position: absolute; left: 604px; top: 0; width: 520px; }
  .product-title { position: absolute; top: 148px; font-weight: 400; font-size: 43px; line-height: 56px; letter-spacing: .5px; white-space: nowrap; }
  .price { position: absolute; top: 222px; font-size: 18px; letter-spacing: 1px; line-height: 24px; }
  .billing { position: absolute; top: 274px; font-size: 19px; color: var(--ink-soft); letter-spacing: .5px; line-height: 26px; white-space: nowrap; }
  .control { position: absolute; top: 324px; font-size: 16px; color: var(--ink-soft); letter-spacing: .5px; line-height: 22px; white-space: nowrap; }
  .buy-button { position: absolute; top: 378px; left: 0; width: 473px; height: 51px; background: var(--button); color: var(--button-text); border: 0; font-family: inherit; font-size: 15.5px; letter-spacing: 1.2px; }
  .description { position: absolute; top: 456px; width: 520px; font-size: 16.5px; line-height: 31px; color: var(--ink-soft); letter-spacing: .5px; }
  .plan-heading { position: absolute; top: 540px; font-size: 16.5px; color: var(--ink-soft); letter-spacing: .5px; line-height: 22px; }
  .plan-list { position: absolute; top: 584px; left: 21px; width: 500px; font-size: 16.5px; line-height: 31px; color: var(--ink-soft); letter-spacing: .5px; }
  .plan-list li { white-space: nowrap; padding-left: 2px; }
  .plan-list strong, .med-note strong { font-weight: 700; color: var(--ink-soft); }
  .med-note { position: absolute; top: 760px; font-size: 16.5px; color: var(--ink-soft); letter-spacing: .5px; line-height: 22px; }
</style>
</head>
<body>
  <header class="site-header">
    <div class="brand">Corvella</div>
    <nav class="nav">
      <a href="#" style="left:0">Testimonials</a>
      <a href="#" style="left:113px">Help<svg class="chev" width="10" height="6" viewBox="0 0 10 6"><path d="M1 1l4 4 4-4" fill="none" stroke="#4a4a4a" stroke-width="1.3"/></svg></a>
      <a href="#" style="left:186px">About</a>
      <a href="#" style="left:253px">Contact</a>
    </nav>
    <div class="header-icons">
      <svg style="left:0" width="24" height="24" viewBox="0 0 24 24"><circle cx="10" cy="10" r="8" fill="none" stroke="#121212" stroke-width="1.6"/><path d="M16 16l6 6" stroke="#121212" stroke-width="1.6"/></svg>
      <svg style="left:47px" width="24" height="24" viewBox="0 0 24 24"><circle cx="12" cy="7" r="5" fill="none" stroke="#121212" stroke-width="1.6"/><path d="M2 23v-3c0-3 3-5 6-5h8c3 0 6 2 6 5v3z" fill="none" stroke="#121212" stroke-width="1.6"/></svg>
      <svg style="left:95px" width="24" height="24" viewBox="0 0 24 24"><rect x="2" y="4" width="20" height="19" rx="3" fill="none" stroke="#121212" stroke-width="1.6"/><path d="M8 4v2a4 4 0 0 0 8 0V4" fill="none" stroke="#121212" stroke-width="1.6"/></svg>
    </div>
  </header>

  <main>
    <section class="product-graphic">
      <div class="photo photo-top" role="img" aria-label="Black and white photo of a woman in a sports top holding a protein shaker in a tiled kitchen"></div>
      <div class="photo photo-side" role="img" aria-label="Continuation of the photo showing the woman's sports top"></div>
      <h2 class="graphic-title">DAILY HARBOR<br>PLAN</h2>
      <div class="includes-tag">Includes</div>
      <ul class="graphic-list">
        <li style="top:0">100% online.<span class="aside">No need to visit the office.</span></li>
        <li style="top:33px">Expert nutrition consult.</li>
        <li style="top:72px">Custom crafted diet plan to achieve your goals.</li>
        <li style="top:111px">Nutrition coaching to improve your health and vitality.</li>
      </ul>
      <p class="graphic-note">*Does not include medication</p>
      <div class="pay-badge" style="padding-left:40px">Month-to-month pay as you go.</div>
      <svg class="pay-icon" width="56" height="56" viewBox="0 0 56 56">
        <circle cx="28" cy="28" r="27" fill="#20c7f1"/>
        <ellipse cx="28" cy="23" rx="12" ry="6" fill="none" stroke="#25235e" stroke-width="2"/>
        <path d="M16 23v6c0 3 5 6 12 6s12-3 12-6v-6" fill="none" stroke="#25235e" stroke-width="2"/>
        <path d="M14 36c3 6 10 9 17 7" fill="none" stroke="#25235e" stroke-width="2"/>
        <path d="M28 40l4 3-4 3" fill="none" stroke="#25235e" stroke-width="2"/>
      </svg>
    </section>

    <section class="product-info">
      <h1 class="product-title">Daily Harbor Plan</h1>
      <p class="price">$99.00</p>
      <p class="billing">No recurring billing</p>
      <p class="control">You're always in control of when you reorder.</p>
      <button class="buy-button">Buy it now</button>
      <p class="description">This plan is designed for people who need to "lose a few pounds", and who want expert consultation for overall health, and vitality.</p>
      <p class="plan-heading">Plan includes:</p>
      <ul class="plan-list">
        <li><strong>100% online</strong>. No need to visit the office.</li>
        <li>Expert nutrition consult</li>
        <li>Custom crafted diet plan to achieve your goals</li>
        <li>Nutrition coaching to improve your health and vitality</li>
        <li>Month-to-month pay as you go</li>
      </ul>
      <p class="med-note"><strong>Does not</strong> include medication</p>
    </section>
  </main>
</body>
</html>
```